mobile app design: app provides timely Natural gas pipeline information (similar to weather, etc)

we are going to create and publish an app in all the three markets.( android, ios,windows). we have wire framed mostly all the screens. the designers are to provide the layout, design & background. The following are the most important things.

1. the app's target audience are guys working in the natural gas industry in the US.
2. the app provides the customer with latest pipeline information
3. the trial version is free and will provide information about one pipeline
4. slides 1 to 5 are trial version slides.
5. slides 6 onwards the customer chooses.
6. the final product is displayed in a grid.
7. the app will be developed using html5 and css3.
8. customer will pay per pipeline for the information. ( in app payment)
9 there are similiar ( complementary) products which provide weekly storage data at vexlo mart and quorbit app store.
10. i have attached the pdf document of the wireframe.
11.i have attached the logo
12. no name has been thought out yet.

Hi guys

I have a main question for the designer community .

1. is it possible to combine some of the pages ( screens  ) into one or two. use your gut feel. if not it is ok.

2. check out the flow, the color, the background , the font and the font size. it should be pleasing.

thanx

Tomek

Natural Gas

```html
<!DOCTYPE html>
<html lang="en">
<head>
<meta charset="utf-8">
<title>Pipeline App Screens</title>
<link href="https://fonts.googleapis.com/css2?family=Dosis:wght@400;500;600&display=swap" rel="stylesheet">
<style>
  :root {
    --canvas: #e6e6e6;
    --sky-top: #bfe8f6;
    --sky-bottom: #5f95dc;
    --red: #d9473a;
    --red-dark: #c23a2e;
    --navy: #3d5b96;
    --navy-dark: #324d82;
    --cyan: #5dbfdb;
    --cyan-dark: #4eaecb;
    --teal: #2f9c88;
    --mint: #86ebbf;
    --mint-line: #b8f3d8;
    --tick: #1f7a5e;
    --header: #3e8da3;
    --cell: #e8f4f6;
    --cell-text: #3fa57d;
    --seg: #4bbde3;
    --white: #ffffff;
    --ink: #123;
  }
  * { box-sizing: border-box; margin: 0; padding: 0; }
  html, body { width: 1200px; height: 720px; overflow: hidden; }
  body {
    background: var(--canvas);
    font-family: "Dosis", sans-serif;
    display: flex; justify-content: center; align-items: center; gap: 60px;
  }
  .screen {
    width: 260px; height: 462px;
    background: linear-gradient(180deg, var(--sky-top) 0%, var(--sky-bottom) 100%);
    display: flex; flex-direction: column; align-items: center;
    box-shadow: 0 10px 30px rgba(0,0,0,.15);
    position: relative;
  }
  .status-bar {
    width: 100%; height: 16px; padding: 0 6px;
    display: flex; justify-content: space-between; align-items: center;
    font-size: 8px; color: #456; font-weight: 500;
  }
  .next-button {
    width: 34px; height: 34px; border-radius: 3px;
    background: var(--teal); border: 1px solid #1f7d6c;
    display: flex; align-items: center; justify-content: center;
  }
  /* Login */
  .login-list { margin-top: 58px; display: flex; flex-direction: column; gap: 10px; }
  .login-button {
    width: 142px; height: 46px; border-radius: 3px;
    display: flex; align-items: center; color: var(--white);
    font-size: 11px; font-weight: 500;
  }
  .login-button .mark-slot { width: 36px; height: 100%; display: flex; align-items: center; justify-content: center; border-right: 1px solid rgba(0,0,0,.15); }
  .login-button .mark-slot span { width: 14px; height: 14px; background: rgba(255,255,255,.85); }
  .login-button .label { flex: 1; text-align: center; }
  .login-nimbra { background: var(--red); border: 1px solid var(--red-dark); }
  .login-sociala { background: var(--navy); border: 1px solid var(--navy-dark); }
  .login-chirpline { background: var(--cyan); border: 1px solid var(--cyan-dark); }
  .screen-login .next-button { margin-top: 24px; }
  /* Regions */
  .region-panel {
    margin-top: 12px; width: 228px;
    background: var(--mint); border: 1px solid var(--mint-line); border-radius: 3px;
  }
  .region-row {
    height: 37px; display: flex; align-items: center; padding: 0 8px;
    border-bottom: 1px solid var(--mint-line);
    color: var(--white); font-size: 14px; font-weight: 500;
  }
  .region-row:last-child { border-bottom: 0; }
  .region-row .check { width: 18px; height: 18px; margin-right: 6px; display: flex; align-items: center; justify-content: center; }
  .region-row .name { flex: 1; }
  .radio { width: 17px; height: 17px; border-radius: 50%; background: var(--white); }
  .screen-regions .next-button { margin-top: 16px; }
  /* Data */
  .segmented {
    margin-top: 14px; display: flex; border: 1px solid var(--seg); border-radius: 3px; overflow: hidden;
    font-size: 12px;
  }
  .segmented span { width: 46px; height: 26px; display: flex; align-items: center; justify-content: center; }
  .segmented .active { background: var(--seg); color: var(--white); }
  .segmented .idle { background: #dff4fb; color: var(--seg); }
  .data-table { margin-top: 4px; width: 100%; border-collapse: collapse; font-size: 10px; }
  .data-table th { background: var(--header); color: var(--white); font-weight: 500; height: 20px; border-right: 1px solid #9cc; }
  .data-table td { background: var(--cell); color: var(--cell-text); text-align: center; height: 12.5px; line-height: 12.5px; border-right: 3px solid #cfe3e7; }
  .add-button {
    margin-top: 12px; padding: 8px 8px; background: var(--cyan); border: 1px solid #8fd8ee;
    border-radius: 3px; color: var(--white); font-size: 11px;
  }
</style>
</head>
<body>

<section class="screen screen-login">
  <div class="status-bar"><span>●●●○○ NOVA</span><span>4:21 PM</span><span>100%</span></div>
  <div class="login-list">
    <div class="login-button login-nimbra"><div class="mark-slot"><span></span></div><div class="label">Login with Nimbra</div></div>
    <div class="login-button login-sociala"><div class="mark-slot"><span></span></div><div class="label">Login with Sociala</div></div>
    <div class="login-button login-chirpline"><div class="mark-slot"><span></span></div><div class="label">Login with Chirpline</div></div>
  </div>
  <div class="next-button"><svg width="14" height="20" viewBox="0 0 14 20"><path d="M3 2 L11 10 L3 18" fill="none" stroke="#fff" stroke-width="3.5"/></svg></div>
</section>

<section class="screen screen-regions">
  <div class="status-bar"><span>●●●○○ NOVA</span><span>4:21 PM</span><span>100%</span></div>
  <div class="region-panel">
    <div class="region-row"><span class="check"><svg width="18" height="16" viewBox="0 0 18 16"><path d="M1 8 L7 14 L17 1" fill="none" stroke="var(--tick)" stroke-width="3"/></svg></span><span class="name">NorthEast</span><svg width="13" height="13" viewBox="0 0 13 13"><circle cx="6.5" cy="6.5" r="6.5" fill="#fff"/><text x="6.5" y="10" text-anchor="middle" font-size="9" font-style="italic" fill="#5a8">i</text></svg></div>
    <div class="region-row"><span class="check"><span class="radio"></span></span><span class="name">MidWest</span><svg width="13" height="13" viewBox="0 0 13 13"><circle cx="6.5" cy="6.5" r="6.5" fill="#fff"/><text x="6.5" y="10" text-anchor="middle" font-size="9" font-style="italic" fill="#5a8">i</text></svg></div>
    <div class="region-row"><span class="check"><svg width="18" height="16" viewBox="0 0 18 16"><path d="M1 8 L7 14 L17 1" fill="none" stroke="var(--tick)" stroke-width="3"/></svg></span><span class="name">SouthEast</span><svg width="13" height="13" viewBox="0 0 13 13"><circle cx="6.5" cy="6.5" r="6.5" fill="#fff"/><text x="6.5" y="10" text-anchor="middle" font-size="9" font-style="italic" fill="#5a8">i</text></svg></div>
    <div class="region-row"><span class="check"><span class="radio"></span></span><span class="name">SouthWest</span><svg width="13" height="13" viewBox="0 0 13 13"><circle cx="6.5" cy="6.5" r="6.5" fill="#fff"/><text x="6.5" y="10" text-anchor="middle" font-size="9" font-style="italic" fill="#5a8">i</text></svg></div>
    <div class="region-row"><span class="check"><span class="radio"></span></span><span class="name">Central</span><svg width="13" height="13" viewBox="0 0 13 13"><circle cx="6.5" cy="6.5" r="6.5" fill="#fff"/><text x="6.5" y="10" text-anchor="middle" font-size="9" font-style="italic" fill="#5a8">i</text></svg></div>
    <div class="region-row"><span class="check"><span class="radio"></span></span><span class="name">West</span><svg width="13" height="13" viewBox="0 0 13 13"><circle cx="6.5" cy="6.5" r="6.5" fill="#fff"/><text x="6.5" y="10" text-anchor="middle" font-size="9" font-style="italic" fill="#5a8">i</text></svg></div>
  </div>
  <div class="next-button"><svg width="14" height="20" viewBox="0 0 14 20"><path d="M3 2 L11 10 L3 18" fill="none" stroke="#fff" stroke-width="3.5"/></svg></div>
</section>

<section class="screen screen-data">
  <div class="status-bar"><span>●●●○○ NOVA</span><span>4:21 PM</span><span>100%</span></div>
  <div class="segmented"><span class="active">Latest</span><span class="idle">Older</span></div>
  <table class="data-table">
    <thead><tr><th>region</th><th>pipeline</th><th>gasday</th><th>postingtime</th></tr></thead>
    <tbody>
      <tr><td>data1</td><td>data1</td><td>data1</td><td>data1</td></tr>
      <tr><td>data1</td><td>data1</td><td>data1</td><td>data1</td></tr>
      <tr><td>data1</td><td>data1</td><td>data1</td><td>data1</td></tr>
      <tr><td>data1</td><td>data1</td><td>data1</td><td>data1</td></tr>
      <tr><td>data1</td><td>data1</td><td>data1</td><td>data1</td></tr>
      <tr><td>data1</td><td>data1</td><td>data1</td><td>data1</td></tr>
      <tr><td>data1</td><td>data1</td><td>data1</td><td>data1</td></tr>
      <tr><td>data1</td><td>data1</td><td>data1</td><td>data1</td></tr>
      <tr><td>data1</td><td>data1</td><td>data1</td><td>data1</td></tr>
      <tr><td>data1</td><td>data1</td><td>data1</td><td>data1</td></tr>
      <tr><td>data1</td><td>data1</td><td>data1</td><td>data1</td></tr>
      <tr><td>data1</td><td>data1</td><td>data1</td><td>data1</td></tr>
      <tr><td>data1</td><td>data1</td><td>data1</td><td>data1</td></tr>
      <tr><td>data1</td><td>data1</td><td>data1</td><td>data1</td></tr>
      <tr><td>data1</td><td>data1</td><td>data1</td><td>data1</td></tr>
    </tbody>
  </table>
  <div class="add-button">Add More Pipelines</div>
</section>

</body>
</html>
```